Banner Design for Websites

I am looking for a few various banner designs of the below size. I want them to look authentic, bold and catchy.
Width 939
Height 262
Wording:
WANTED: DRIVEN AND SUCCESSFUL INDIVIDUALS READY TO TAKE THEIR RESULTS TO THE NEXT LEVEL.

Make up to $5000 per sale
No cold calling
No experience required
No pressure selling
NOT MLM

Personal Empowerment. The Next Big Business Boom !

I make well in excess of 10k per month consistently. Brenda K

Some photos attached for use and also some others banners for various workding other than above.

```html
<!DOCTYPE html>
<html lang="en">
<head>
<meta charset="utf-8">
<title>Personal Empowerment Banner</title>
<link rel="stylesheet" href="https://fonts.googleapis.com/css2?family=Alegreya+Sans:ital,wght@1,800;1,900&family=Dosis:wght@600&display=swap">
<style>
  :root {
    --blue-deep: #2e3590;
    --blue-mid: #1a56a8;
    --blue-bright: #0a70c0;
    --green: #3bb54a;
    --white: #ffffff;
    --quote-blue: #0f6db8;
    --photo-warm: #8a5a3c;
    --photo-dark: #4a3328;
  }
  html, body {
    margin: 0;
    width: 1200px;
    height: 1000px;
    overflow: hidden;
    background: var(--white);
  }
  .banner {
    position: absolute;
    left: 130px;
    top: 369px;
    width: 939px;
    height: 262px;
    font-family: "Alegreya Sans", sans-serif;
    font-style: italic;
    font-weight: 800;
  }
  .banner-backdrop {
    position: absolute;
    inset: 0;
  }
  .wanted-box {
    position: absolute;
    left: 25px;
    top: 23px;
    width: 227px;
    height: 176px;
    border: 3px solid var(--green);
    border-radius: 10px;
    color: var(--white);
    text-align: center;
    font-size: 18px;
    line-height: 23.5px;
    display: flex;
    align-items: center;
    justify-content: center;
    text-transform: uppercase;
  }
  .benefit-list {
    position: absolute;
    left: 297px;
    top: 50px;
    margin: 0;
    padding: 0;
    list-style: none;
    color: var(--white);
    font-size: 21px;
    line-height: 28px;
  }
  .benefit-list li::before {
    content: "> ";
    color: var(--green);
  }
  .testimonial {
    position: absolute;
    left: 587px;
    top: 8px;
    width: 220px;
    margin: 0;
    color: var(--quote-blue);
    text-align: center;
    font-size: 17.5px;
    line-height: 24.5px;
  }
  .testimonial-author {
    display: block;
    margin-top: 24px;
  }
  .cta-button {
    position: absolute;
    left: 593px;
    top: 159px;
    width: 203px;
    height: 45px;
    border-radius: 10px;
    background: var(--green);
    color: var(--white);
    font-size: 17.5px;
    display: flex;
    align-items: center;
    justify-content: center;
    text-decoration: none;
  }
  .tagline-band {
    position: absolute;
    left: 0;
    top: 226px;
    width: 939px;
    height: 36px;
    background: var(--green);
    color: var(--white);
    font-family: "Dosis", sans-serif;
    font-style: normal;
    font-weight: 600;
    font-size: 33px;
    letter-spacing: 1px;
    text-transform: uppercase;
    text-align: center;
    line-height: 36px;
  }
</style>
</head>
<body>
  <div class="banner">
    <svg class="banner-backdrop" width="939" height="262" viewBox="0 0 939 262">
      <defs>
        <linearGradient id="mainBlue" x1="0" y1="0" x2="1" y2="0">
          <stop offset="0" stop-color="var(--blue-deep)"/>
          <stop offset="0.55" stop-color="var(--blue-mid)"/>
          <stop offset="1" stop-color="var(--blue-bright)"/>
        </linearGradient>
        <linearGradient id="photoTone" x1="0" y1="0" x2="0" y2="1">
          <stop offset="0" stop-color="var(--photo-warm)"/>
          <stop offset="1" stop-color="var(--photo-dark)"/>
        </linearGradient>
      </defs>
      <rect class="main-field" x="0" y="0" width="939" height="226" fill="url(#mainBlue)"/>
      <circle class="quote-bubble" cx="697" cy="24" r="119" fill="var(--white)"/>
      <path class="photo-edge" d="M815 0 Q852 120 788 226 L939 226 L939 0 Z" fill="var(--white)"/>
      <path class="team-photo" role="img" aria-label="Photo of two smiling team members wearing event badges at a conference"
            d="M831 0 Q862 120 806 226 L939 226 L939 0 Z" fill="url(#photoTone)"/>
    </svg>

    <div class="wanted-box">
      <p style="margin:0">Wanted:<br>Driven and successful<br>individuals<br>ready to take<br>their results<br>to the<br>next level</p>
    </div>

    <ul class="benefit-list">
      <li>Make up to $5000 per sale</li>
      <li>No cold calling</li>
      <li>No experience required</li>
      <li>No pressure selling</li>
      <li>NOT MLM</li>
    </ul>

    <blockquote class="testimonial">
      “I make well in excess<br>of 10k per month<br>consistently.”
      <span class="testimonial-author">Brenda K</span>
    </blockquote>

    <a class="cta-button" href="#">Click Here for More Info</a>

    <div class="tagline-band">Personal Empowerment. The Next Big Business Boom !</div>
  </div>
</body>
</html>
```